First Aid Training business needs business card design

We would like a double sided business card designed for a first aid training business - Brindlewood First Aid. We provide first aid training and , WHS (work, health and safety) training.

The attached word document contains the key information we would like on each side of the business card.

Final design needs to be delivered in print ready format, along with the original file.

```html
<!DOCTYPE html>
<html lang="en">
<head>
<meta charset="utf-8">
<title>Brindlewood First Aid – Business Card</title>
<link href="https://fonts.googleapis.com/css2?family=Montserrat:wght@600&family=Open+Sans:ital,wght@0,400;0,700;1,700&display=swap" rel="stylesheet">
<style>
  :root {
    --stage: #2b2b2b;
    --card-dark: #1c1c1c;
    --card-light: #ffffff;
    --red: #e92227;
    --grey: #8a8a8a;
    --ink: #333333;
    --white: #ffffff;
  }
  * { box-sizing: border-box; margin: 0; padding: 0; }
  html, body { width: 1200px; height: 900px; overflow: hidden; }
  body {
    background: var(--stage);
    font-family: "Open Sans", sans-serif;
    display: flex;
    flex-direction: column;
    align-items: center;
    justify-content: center;
    gap: 40px;
  }
  .card {
    position: relative;
    width: 700px;
    height: 400px;
    overflow: hidden;
    box-shadow: 0 10px 30px rgba(0,0,0,.45);
  }

  /* Front */
  .card--front { background: var(--card-light); }
  .card__swoosh { position: absolute; inset: 0; width: 100%; height: 100%; }
  .brand {
    position: absolute;
    left: 70px;
    top: 150px;
    display: flex;
    align-items: center;
    gap: 14px;
  }
  .brand__dot {
    width: 40px; height: 40px; border-radius: 50%;
    background: var(--red);
  }
  .brand__name {
    font-family: "Montserrat", sans-serif;
    font-weight: 600;
    font-size: 22px;
    color: var(--ink);
    text-transform: uppercase;
    letter-spacing: 1px;
    line-height: 1.1;
    width: 210px;
  }
  .divider {
    position: absolute;
    left: 355px; top: 130px;
    width: 2px; height: 130px;
    background: var(--red);
  }
  .contact {
    position: absolute;
    left: 380px; top: 140px;
  }
  .contact__name {
    font-weight: 700;
    font-style: italic;
    font-size: 26px;
    color: var(--red);
    text-transform: uppercase;
    margin-bottom: 10px;
  }
  .contact__line {
    display: flex; align-items: center; gap: 8px;
    font-size: 15px; color: var(--ink); line-height: 1.7;
  }
  .contact__icon { width: 14px; height: 14px; flex: none; }

  /* Back */
  .card--back { background: var(--card-dark); color: var(--white); }
  .back__content { position: absolute; left: 50px; top: 45px; }
  .back__name {
    font-family: "Montserrat", sans-serif;
    font-weight: 600;
    font-size: 34px;
    text-transform: uppercase;
    letter-spacing: 1px;
    line-height: 1.1;
    margin-bottom: 22px;
  }
  .back__tagline {
    color: var(--red);
    font-weight: 700;
    font-style: italic;
    font-size: 19px;
    text-transform: uppercase;
    line-height: 1.3;
    margin-bottom: 10px;
  }
  .benefits { list-style: none; font-size: 17px; line-height: 1.5; margin-bottom: 22px; }
  .benefits li::before,
  .services__sep {
    content: "";
    display: inline-block;
    width: 8px; height: 8px; border-radius: 50%;
    background: var(--red);
    margin-right: 10px;
    vertical-align: middle;
  }
  .services { font-size: 17px; }
  .services__sep { margin: 0 10px; }
  .back__mark {
    position: absolute;
    right: -70px; top: 120px;
    width: 320px; height: 320px;
    border-radius: 50%;
    background: linear-gradient(135deg, #8a8a8a, #5a5a5a);
  }
</style>
</head>
<body>

  <section class="card card--front" aria-label="Business card front">
    <svg class="card__swoosh" viewBox="0 0 700 400" preserveAspectRatio="none" aria-hidden="true">
      <path d="M0 60 Q110 55 200 120" fill="none" stroke="var(--red)" stroke-width="6"/>
      <path d="M0 72 Q100 70 180 125" fill="none" stroke="var(--red)" stroke-width="1.5"/>
      <path d="M430 335 Q560 360 700 340" fill="none" stroke="var(--red)" stroke-width="1.5"/>
      <path d="M410 345 Q560 385 700 360" fill="none" stroke="var(--red)" stroke-width="6"/>
    </svg>

    <div class="brand">
      <span class="brand__dot"></span>
      <span class="brand__name">Brindlewood First Aid</span>
    </div>

    <div class="divider"></div>

    <div class="contact">
      <p class="contact__name">Dana Mercer</p>
      <p class="contact__line">
        <svg class="contact__icon" viewBox="0 0 24 24" aria-hidden="true"><path fill="var(--red)" d="M6.6 10.8a15 15 0 0 0 6.6 6.6l2.2-2.2c.3-.3.7-.4 1-.2 1.1.4 2.3.6 3.6.6.6 0 1 .4 1 1V20c0 .6-.4 1-1 1A17 17 0 0 1 3 4c0-.6.4-1 1-1h3.5c.6 0 1 .4 1 1 0 1.3.2 2.5.6 3.6.1.3 0 .7-.2 1z"/></svg>
        0400 123 456
      </p>
      <p class="contact__line">
        <svg class="contact__icon" viewBox="0 0 24 24" aria-hidden="true"><path fill="var(--red)" d="M2 5h20v14H2z"/><path fill="none" stroke="#fff" stroke-width="2" d="M2 6l10 7 10-7"/></svg>
        help@brindlewoodfirstaid.com.au
      </p>
      <p class="contact__line">
        <svg class="contact__icon" viewBox="0 0 24 24" aria-hidden="true"><circle cx="12" cy="12" r="10" fill="var(--red)"/><path fill="none" stroke="#fff" stroke-width="1.5" d="M2 12h20M12 2c3 3 3 17 0 20M12 2c-3 3-3 17 0 20"/></svg>
        brindlewoodfirstaid.com.au
      </p>
    </div>
  </section>

  <section class="card card--back" aria-label="Business card back">
    <div class="back__content">
      <h1 class="back__name">Brindlewood<br>First Aid</h1>
      <p class="back__tagline">Onsite training<br>We can come to you</p>
      <ul class="benefits">
        <li>Time efficient</li>
        <li>Cost effective</li>
        <li>Minimise downtime for your team</li>
      </ul>
      <p class="services">First Aid Training<span class="services__sep"></span>WHS Training</p>
    </div>
    <div class="back__mark" aria-hidden="true"></div>
  </section>

</body>
</html>
```